Design for social media advertising campaign

Multiple designs to be produced for a legal services advertising campaign in Australia offering assistance to small to medium sized businesses facing financial issues arising from the economic consequences of Covid-19. Designs must be sized suitably for LinkedIn, Twitter and Facebook. See our website recovery.harbourline.example and Facebook page KellowayLaw.CoastCounsel for logo, colours etc. Examples of the messaging is in the 5 uploaded files.

Target Market(s)

Small / medium size business owners

Industry/Entity Type

Legal

Requirements
Must have
• Sizing for Facebook, LinkedIn and Twitter

```html
<!DOCTYPE html>
<html lang="en">
<head>
<meta charset="utf-8">
<title>Facing Business Solvency Issues? – Harbourline Recovery Lawyers</title>
<link rel="stylesheet" href="https://fonts.googleapis.com/css2?family=Jost:wght@400&family=Roboto+Condensed:wght@800&family=Roboto:wght@700;900&display=swap">
<style>
  :root {
    --maroon: #7f0020;
    --gold: #d3ad3b;
    --white: #ffffff;
    --window: #f4f5f3;
    --desk: #d8cfc2;
    --desk-deep: #c9bcaa;
    --chair: #d9c7a2;
    --suit: #2c2624;
    --laptop: #eeeeee;
  }
  * { margin: 0; padding: 0; box-sizing: border-box; }
  html, body {
    width: 1200px;
    height: 737px;
    overflow: hidden;
    background: var(--maroon);
  }
  .ad {
    position: relative;
    width: 1200px;
    height: 737px;
    background: var(--maroon);
  }
  .ad__panel {
    position: absolute;
    left: 72px;
    top: 72px;
    width: 1056px;
    height: 594px;
    background: var(--white);
    overflow: hidden;
  }
  .ad__photo {
    position: absolute;
    inset: 0;
    background:
      linear-gradient(90deg, var(--white) 0%, rgba(255,255,255,0.96) 30%, rgba(255,255,255,0.55) 46%, rgba(255,255,255,0) 60%),
      radial-gradient(ellipse 150px 120px at 700px 450px, rgba(238,238,238,0.95), rgba(238,238,238,0) 100%),
      radial-gradient(ellipse 230px 260px at 840px 380px, rgba(44,38,36,0.92) 0%, rgba(44,38,36,0.75) 45%, rgba(44,38,36,0) 100%),
      radial-gradient(ellipse 110px 240px at 1030px 420px, rgba(217,199,162,0.9), rgba(217,199,162,0) 100%),
      linear-gradient(180deg, rgba(216,207,194,0) 0%, rgba(216,207,194,0) 82%, var(--desk) 86%, var(--desk-deep) 100%),
      linear-gradient(180deg, var(--window) 0%, #ebe9e5 100%);
  }
  .ad__text {
    position: absolute;
    left: 98px;
    color: var(--maroon);
    line-height: 1;
    white-space: nowrap;
  }
  .ad__lead {
    top: 111px;
    font-family: "Jost", sans-serif;
    font-weight: 400;
    font-size: 42px;
  }
  .ad__headline {
    font-family: "Roboto Condensed", sans-serif;
    font-weight: 800;
    font-size: 91px;
    letter-spacing: -0.5px;
  }
  .ad__headline--first { top: 152px; }
  .ad__headline--second { top: 226px; }
  .ad__tail {
    top: 318px;
    font-family: "Jost", sans-serif;
    font-weight: 400;
    font-size: 36px;
    letter-spacing: 1px;
  }
  .ad__cta {
    top: 383px;
    font-family: "Roboto", sans-serif;
    font-weight: 900;
    font-size: 31px;
    line-height: 32px;
    letter-spacing: 1px;
    color: var(--gold);
  }
  .ad__firm {
    top: 517px;
    font-family: "Roboto", sans-serif;
    font-weight: 700;
    font-size: 21px;
    letter-spacing: 0.3px;
  }
</style>
</head>
<body>
  <main class="ad">
    <section class="ad__panel">
      <div class="ad__photo" role="img" aria-label="Photo of a worried businessman in a dark suit sitting at a desk with a laptop, hands pressed together, in a bright office"></div>
      <p class="ad__text ad__lead">Facing</p>
      <h1 class="ad__text ad__headline ad__headline--first">BUSINESS</h1>
      <h1 class="ad__text ad__headline ad__headline--second">SOLVENCY</h1>
      <p class="ad__text ad__tail">ISSUES?</p>
      <p class="ad__text ad__cta">OBTAIN OUR FREE GUIDE<br>NOW</p>
      <p class="ad__text ad__firm">Harbourline Recovery Lawyers</p>
    </section>
  </main>
</body>
</html>
```